I want our new logo design to guide the colors and look of the home page. I want it to be vibrant and contemporary. We are a new religious education publishing company. I would like any colors used to describe the product below to be bright and cheerful, but also to look good with our logo colors
On our home page we are introducing a new product for second graders. The product name should look child friendly, but not silly. If there is a way to add reverence to the words FIRST RECONCILIATION and FIRST EUCHARIST, and still make it look like it is a product for children, that would be great.
The product will be called:
Little Pilgrim Learning Set for the Open Door Room
FIRST RECONCILIATION
FIRST EUCHARIST
THE PRODUCT DESCRIPTION SHOULD BE AS FOLLOWS
Field tested and designed for the special needs inclusive classroom
Kit includes high impact visuals, hands-on activities, manipulatives, games, and other teaching aids for total engagement of ALL students
Detailed catechist lesson plans to maximize learning and retention
Cost effective reusable kit
Bilingual
Somewhere it should say COMING SOON, because the product is not ready yet, but we are promoting it. I don't have a picture of this product yet, but above the product description, we need an empty box that we'll use when we're ready to upload the picture of the kit.
There should also be a statement near the product description that says: To learn more about the Little Pilgrim Set for the Open Door Room, click here.
Web page links:
About Us
Products
Resources
Contact Us
I would also like a few links to be featured on the home page:
Faith Lessons for Tomorrow's Hearts....learn more
"Where Do We Begin?"....learn more
Could It Be Something Deeper Inside?...learn more
The Dream and the Daily...learn more
Genuine Welcoming Formation
I have increased my budget and clarified my brief so that it's easier to understand. It's basically just a home page and a template for the other pages. There is no content on the other web pages that you have to work on. I just need a well designed home page and a nice template for the other pages.
Reason: I am extending the deadline for 2 days so that templates can be designed for 5 additional web pages. Please make each template a little different from the way you designed the home page. These pages can have blank picture boxes and dummy text to save you time. I am only interested in layout for the addtional pages. Thank you!
We've made a selection and wanted to thank all of you for your wonderful designs!

```html
<!DOCTYPE html>
<html lang="en">
<head>
<meta charset="utf-8">
<title>Bright Shore Catechetics – Home</title>
<link href="https://fonts.googleapis.com/css2?family=Exo+2:wght@300&family=Nunito:wght@800;900&family=Open+Sans:wght@400;600;700&display=swap" rel="stylesheet">
<style>
:root{
  --brown:#4b2f12;
  --footer:#221a10;
  --cream:#efe8dc;
  --orange:#f7a21b;
  --red:#c0202e;
  --blue:#2b9be3;
  --blue-dark:#1781cf;
  --text:#6b6b6b;
  --heading:#6e6e6e;
  --light:#f5f5f5;
  --footer-text:#8a7a62;
  --footer-head:#a8998a;
  --rule:#5a4a36;
}
*{margin:0;padding:0;box-sizing:border-box}
html,body{width:999px;height:1200px;overflow:hidden}
body{position:relative;background:#fff;font-family:"Open Sans",sans-serif;color:var(--text)}
.abs{position:absolute}

/* Header */
.site-header{left:0;top:0;width:999px;height:162px;background:var(--brown)}
.brand{left:0;width:999px;text-align:center}
.brand-mark{left:485px;top:26px;width:28px;height:28px;border-radius:50%;background:var(--orange)}
.brand-name{top:92px;font-size:29px;font-weight:600;color:var(--orange)}
.brand-tagline{top:128px;font-size:16px;color:#b39a7e;padding-left:60px}

/* Navigation */
.main-nav{left:0;top:162px;width:999px;height:73px;display:flex;justify-content:center;gap:36px;padding-top:25px;padding-right:24px}
.main-nav a{font-size:19px;color:#4b3018;text-decoration:none;height:28px}
.main-nav a.current{border-bottom:2px solid var(--red)}

/* Hero */
.hero{left:0;top:235px;width:999px;height:540px;background:var(--cream)}
.hero-card{left:61px;top:16px;width:875px;height:505px;background:#fbfbfa;border:1px solid #e0d8cc}
.hero-title{left:0;top:0;width:873px;height:56px;background:var(--orange);color:#fff;font-family:"Exo 2",sans-serif;font-weight:300;font-size:38px;text-align:center;line-height:56px}
.kit-visual{left:41px;top:109px;width:210px;height:286px;border-radius:3px;background:linear-gradient(90deg,#ffd9a3,#ffe9cc 60%,#f7c78a)}
.ribbon{left:-10px;top:392px}
.product-name{left:302px;top:112px;width:560px;font-family:"Nunito",sans-serif;font-weight:900;font-size:32px;line-height:38px;color:var(--blue)}
.features{left:312px;top:197px;width:493px;list-style:none;font-size:18px;line-height:18px;letter-spacing:.4px;color:#555}
.features li{position:relative;padding-left:13px;margin-bottom:8px}
.features li::before{content:"";position:absolute;left:0;top:6px;width:6px;height:6px;border-radius:50%;background:#666}
.btn{height:42px;border-radius:5px;background:linear-gradient(#4bb2f0,var(--blue-dark));color:#fff;font-family:"Nunito",sans-serif;font-weight:800;text-align:center;line-height:42px;box-shadow:0 3px 4px rgba(0,0,0,.25);text-decoration:none}
.btn-learn{left:312px;top:420px;width:182px;font-size:22px}
.btn-notify{left:516px;top:420px;width:297px;font-size:17px}

/* Info band */
.info{left:0;top:775px;width:999px;height:263px;background:var(--light)}
.info h2{font-size:15px;font-weight:700;color:var(--heading)}
.intro{left:79px;top:26px;width:462px}
.intro p{margin-top:6px;font-size:12.2px;line-height:15.5px}
.divider-v{border-left:1px dotted #c8c8c8}
.info-divider{left:562px;top:40px;height:121px}
.link-list{left:581px;top:26px;width:360px}
.link-list ul{list-style:none;margin-top:4px;font-size:12.2px;line-height:19px}
.info strong{font-weight:700;color:#555}

/* Footer */
.site-footer{left:0;top:1038px;width:999px;height:162px;background:var(--footer)}
.site-footer h3{font-size:19px;font-weight:700;color:var(--footer-head)}
.site-footer p{font-size:12.6px;line-height:19.5px;color:var(--footer-text)}
.foot-contact{left:60px;top:20px}
.foot-contact p{margin-top:8px}
.foot-brand{left:324px;top:20px}
.foot-brand .foot-links{margin-top:8px;line-height:23px}
.foot-brand .copy{margin-top:10px}
.foot-find{left:833px;top:20px}
.social{display:flex;gap:12px;margin-top:14px}
.social span{width:27px;height:27px;border-radius:2px}
.social .s1{background:#3b5a98}
.social .s2{background:#4fb5df}
.foot-div1{left:296px;top:24px;height:110px;border-color:var(--rule)}
.foot-div2{left:806px;top:24px;height:110px;border-color:var(--rule)}
</style>
</head>
<body>
<header class="site-header abs">
  <span class="brand-mark abs"></span>
  <div class="brand brand-name abs">Bright Shore Catechetics</div>
  <div class="brand brand-tagline abs">a new approach to catechesis</div>
</header>

<nav class="main-nav abs">
  <a class="current" href="#">HOME</a>
  <a href="#">ABOUT US</a>
  <a href="#">PRODUCTS</a>
  <a href="#">RESOURCES</a>
  <a href="#">CONTACT US</a>
</nav>

<section class="hero abs" role="img" aria-label="Soft cream background with faint scattered children's handprints">
  <div class="hero-card abs">
    <h1 class="hero-title abs">First Reconciliation and First Eucharist</h1>
    <div class="kit-visual abs" role="img" aria-label="Product box picture of the learning kit, coming soon"></div>
    <svg class="ribbon abs" width="300" height="48" viewBox="0 0 300 48" aria-hidden="true">
      <polygon points="0,8 10,0 10,8" fill="#7a1018"/>
      <polygon points="0,8 293,8 272,25 293,42 0,42" fill="#c0202e"/>
      <text x="153" y="33" text-anchor="middle" font-family="Nunito, sans-serif" font-weight="900" font-size="23" fill="#fff">Coming soon!</text>
    </svg>
    <h2 class="product-name abs">Little Pilgrim Learning Set for the Open Door Room</h2>
    <ul class="features abs">
      <li>Field tested and designed for the special needs inclusive classroom</li>
      <li>Kit includes high impact visuals, hands-on activities, manipulatives, games, and other teaching aids for total engagement of ALL students</li>
      <li>Detailed catechist lesson plans to maximize learning and retention</li>
      <li>Cost effective reusable kit</li>
      <li>Bilingual</li>
    </ul>
    <a class="btn btn-learn abs" href="#">Learn more</a>
    <a class="btn btn-notify abs" href="#">Notify me when available</a>
  </div>
</section>

<section class="info abs">
  <div class="intro abs">
    <h2>A new approach to catechesis</h2>
    <p>There are many variations of passages of Lorem Ipsum available, but the majority have suffered alteration in some form, by injected humour, or randomised words which don't look even slightly believable. If you are going to use a passage of Lorem Ipsum, you need to be sure there isn't anything embarrassing hidden in the middle of text. All the Lorem Ipsum generators on the Internet tend to repeat predefined chunks as necessary, making this the first true generator on the Internet. It uses a dictionary of over 200 Latin words, combined with a handful of model sentence structures, to generate Lorem Ipsum which looks reasonable. The generated Lorem Ipsum is therefore always free from repetition, injected humour, or non-characteristic words etc. <strong>Read more...</strong></p>
  </div>
  <div class="divider-v info-divider abs"></div>
  <div class="link-list abs">
    <h2>Another heading</h2>
    <ul>
      <li>Faith lessons for tomorrow's hearts. <strong>Learn more...</strong></li>
      <li>"Where do we begin?" <strong>Learn more...</strong></li>
      <li>Could it be something deeper inside? <strong>Learn more...</strong></li>
      <li>The Dream and the Daily. <strong>Learn more...</strong></li>
      <li>Genuine welcoming formation. <strong>Learn more...</strong></li>
    </ul>
  </div>
</section>

<footer class="site-footer abs">
  <div class="foot-contact abs">
    <h3>CONTACT</h3>
    <p>14 Harbour Lane<br>Easton NSW 2990<br>555.010.246<br>info@brightshorecatechetics.com</p>
  </div>
  <div class="divider-v foot-div1 abs"></div>
  <div class="foot-brand abs">
    <h3>BRIGHT SHORE CATECHETICS</h3>
    <p class="foot-links">HOME &nbsp;| &nbsp;ABOUT US &nbsp;| &nbsp;PRODUCTS &nbsp;| &nbsp;RESOURCES &nbsp;| CONTACT US<br>PRIVACY &nbsp;| &nbsp;SITE MAP</p>
    <p class="copy">© 2011 Bright Shore Catechetics</p>
  </div>
  <div class="divider-v foot-div2 abs"></div>
  <div class="foot-find abs">
    <h3>FIND US</h3>
    <div class="social">
      <span class="s1" role="img" aria-label="Social network link"></span>
      <span class="s2" role="img" aria-label="Social network link"></span>
    </div>
  </div>
</footer>
</body>
</html>
```